Global (re)insurance broker needs a business card design

We need a classic business card for our company that is headquartered in SG, with offices in Malaysia and Dubai. We specialise in insurance and reinsurance broking and consultancy for our global clients.

```html
<!DOCTYPE html>
<html lang="en">
<head>
<meta charset="utf-8">
<title>Veldmark business card</title>
<link rel="stylesheet" href="https://fonts.googleapis.com/css2?family=Open+Sans:wght@400;600;700&display=swap">
<style>
  :root {
    --page: #2a2a2d;
    --card: #1f1f24;
    --blue: #2446a0;
    --mint: #c3dfb9;
    --ink: #ffffff;
    --rule: #9a9aa0;
  }
  * { box-sizing: border-box; margin: 0; padding: 0; }
  html, body {
    width: 1200px; height: 780px; overflow: hidden;
    background: var(--page);
    font-family: "Open Sans", Arial, sans-serif;
  }
  .sheet {
    width: 1200px; height: 780px;
    display: flex; align-items: center; justify-content: center; gap: 40px;
  }
  .card {
    position: relative;
    width: 540px; height: 309px;
    background: var(--card);
    border-radius: 26px;
    overflow: hidden;
    box-shadow: 0 14px 30px rgba(0,0,0,.45);
  }
  .card__band { position: absolute; left: 0; bottom: 0; width: 540px; height: 20px; display: block; }
  .brand-name {
    font-weight: 700; color: var(--mint); letter-spacing: 2px; line-height: 1;
  }
  /* front */
  .front .brand-name { position: absolute; left: 34px; top: 52px; font-size: 40px; }
  .front .divider { position: absolute; left: 0; top: 0; }
  .person { position: absolute; left: 300px; top: 112px; }
  .person__name { font-size: 27px; font-weight: 700; color: var(--blue); line-height: 1.1; }
  .person__name .surname { color: var(--mint); }
  .person__role { font-size: 14px; color: var(--ink); margin-top: 2px; }
  .contacts { list-style: none; margin-top: 12px; }
  .contacts li { display: flex; align-items: center; gap: 8px; font-size: 13px; color: var(--ink); line-height: 1.6; }
  .contacts svg { width: 12px; height: 12px; flex: none; }
  .address {
    position: absolute; left: 30px; bottom: 34px;
    font-size: 13px; color: var(--ink);
  }
  /* back */
  .back .brand-name {
    position: absolute; left: 0; right: 0; top: 118px;
    text-align: center; font-size: 58px; letter-spacing: 4px;
  }
</style>
</head>
<body>
<main class="sheet">
  <section class="card front">
    <div class="brand-name">VELDMARK</div>
    <svg class="divider" width="540" height="309" aria-hidden="true">
      <line x1="300" y1="70" x2="250" y2="240" stroke="var(--rule)" stroke-width="1"/>
    </svg>
    <div class="person">
      <h1 class="person__name">Mira <span class="surname">Castellan</span></h1>
      <p class="person__role">Chief Operating Officer</p>
      <ul class="contacts">
        <li>
          <svg viewBox="0 0 12 12" aria-hidden="true"><rect x="3" y="0.5" width="6" height="11" rx="1" fill="none" stroke="var(--mint)"/></svg>
          +65 9000 4127
        </li>
        <li>
          <svg viewBox="0 0 12 12" aria-hidden="true"><circle cx="6" cy="6" r="5.5" fill="var(--blue)"/><path d="M0.5 6h11M6 0.5v11" stroke="var(--card)" stroke-width=".8"/></svg>
          www.veldmark.com
        </li>
        <li>
          <svg viewBox="0 0 12 12" aria-hidden="true"><rect x="0.5" y="2.5" width="11" height="7" fill="none" stroke="var(--mint)"/><path d="M0.5 2.5l5.5 4 5.5-4" fill="none" stroke="var(--mint)"/></svg>
          mira@veldmark.com
        </li>
      </ul>
    </div>
    <p class="address">24 Harbour Lane, Meridian Tower #08-03, Singapore 048812</p>
    <svg class="card__band" viewBox="0 0 540 20" aria-hidden="true">
      <polygon points="0,0 212,0 220,20 0,20" fill="var(--blue)"/>
      <polygon points="232,0 540,0 540,20 240,20" fill="var(--mint)"/>
    </svg>
  </section>

  <section class="card back">
    <div class="brand-name">VELDMARK</div>
    <svg class="card__band" viewBox="0 0 540 20" aria-hidden="true">
      <polygon points="0,0 212,0 220,20 0,20" fill="var(--blue)"/>
      <polygon points="232,0 540,0 540,20 240,20" fill="var(--mint)"/>
    </svg>
  </section>
</main>
</body>
</html>
```